Business Card for beauty technology startup

Design Glowmi Business Card for a Beauty, based on the website identity and colors (https://www.glowmi-example.com).
Glowmi is a beauty tech startup that gathers helpful product info for beauty lovers and consumers (such as availability on stores, price range and product reviews) for makeup products. The card design must be young, colorful but clean, and very modern.

Target Market(s)

woman, 15-35

Industry/Entity Type

Cosmetics

Contact Information for Business Card

Full Name, address, phone

Font styles to use
Other font styles liked:
• Advent Pro

Colors
e34297
86cfc6
ffffff
5c5c5c
e8e8e8
e667a6
b2b2b2

Requirements
Must have
• One full colored side with a creative design and another with card info
• Use Color palette: #95C5C5 and/or #D38AA5
• Use fonts: Advent Pro
• Use website identity: https://www.glowmi-example.com
Nice to have
• If needed extra font: Roboto

```html
<!DOCTYPE html>
<html lang="pt">
<head>
<meta charset="utf-8">
<title>Glowmi — Cartão de visita</title>
<link rel="stylesheet" href="https://fonts.googleapis.com/css2?family=Advent+Pro:wght@200;300;700&family=Roboto+Slab:wght@300&display=swap">
<style>
  :root {
    --canvas: #f2f2f2;
    --teal: #6ad3cb;
    --pink: #ff3d9c;
    --white: #ffffff;
    --photo-light: #8fdcd4;
    --photo-mid: #d9c8bc;
    --photo-dark: #2f3b3a;
  }
  * { margin: 0; padding: 0; box-sizing: border-box; }
  html, body {
    width: 1200px; height: 1200px; overflow: hidden;
    background: var(--canvas);
  }
  .sheet {
    width: 1200px; height: 1200px;
    display: flex; flex-direction: column; align-items: center; justify-content: center;
    gap: 56px;
  }
  .card {
    position: relative;
    width: 900px; height: 514px;
    border-radius: 26px;
    overflow: hidden;
    color: var(--white);
    box-shadow: 0 10px 30px rgba(0,0,0,0.12);
  }

  /* Front */
  .card--front { background: var(--teal); }
  .front-brand {
    position: absolute; left: 92px; top: 50%;
    transform: translateY(-50%);
    display: flex; align-items: center; gap: 34px;
  }
  .brand-dot {
    width: 110px; height: 110px; border-radius: 50%;
    border: 3px solid var(--white);
    flex: none;
  }
  .front-wordmark {
    font-family: "Advent Pro", sans-serif;
    font-weight: 200;
    font-size: 96px;
    letter-spacing: 12px;
    text-transform: uppercase;
  }
  .front-photo {
    position: absolute; right: 0; top: 0;
    width: 270px; height: 100%;
    background:
      linear-gradient(180deg, transparent 78%, var(--photo-dark) 78%),
      radial-gradient(ellipse at 50% 30%, var(--photo-mid) 0%, var(--photo-light) 75%);
  }

  /* Back */
  .card--back { background: var(--pink); }
  .back-brand {
    position: absolute; right: 60px; top: 44px;
    display: flex; align-items: center; gap: 16px;
  }
  .brand-dot--small { width: 58px; height: 58px; border-width: 2px; }
  .back-wordmark {
    font-family: "Advent Pro", sans-serif;
    font-weight: 300;
    font-size: 46px;
    letter-spacing: 4px;
  }
  .contact {
    position: absolute; left: 132px; top: 228px;
  }
  .contact-name {
    font-family: "Advent Pro", sans-serif;
    font-weight: 700;
    font-size: 30px;
    letter-spacing: 3px;
    text-transform: uppercase;
  }
  .contact-role {
    font-family: "Advent Pro", sans-serif;
    font-weight: 700;
    font-size: 22px;
    letter-spacing: 2px;
    margin: 10px 0 0 20px;
  }
  .contact-lines {
    list-style: none;
    margin: 40px 0 0 60px;
    font-family: "Roboto Slab", serif;
    font-weight: 300;
    font-size: 22px;
    line-height: 1.35;
  }
</style>
</head>
<body>
  <main class="sheet">
    <section class="card card--front" aria-label="Frente do cartão">
      <div class="front-brand">
        <span class="brand-dot" aria-hidden="true"></span>
        <span class="front-wordmark">Glowmi</span>
      </div>
      <div class="front-photo" role="img" aria-label="Fotografia de uma jovem modelo de blusa branca sobre fundo turquesa"></div>
    </section>

    <section class="card card--back" aria-label="Verso do cartão">
      <div class="back-brand">
        <span class="back-wordmark">Glowmi</span>
        <span class="brand-dot brand-dot--small" aria-hidden="true"></span>
      </div>
      <div class="contact">
        <p class="contact-name">Nome Completo</p>
        <p class="contact-role">CEO</p>
        <ul class="contact-lines">
          <li>Celular:(00)0000-0000</li>
          <li>contato@glowmi-example.com</li>
          <li>https://www.glowmi-example.com/</li>
        </ul>
      </div>
    </section>
  </main>
</body>
</html>
```